New young doctors office business card

Doctor's office
Hello:
My name is Dr. Mateo Anselmo Quiroga Benítez. I need a business card for my new office located within a hospital. The name of the hospital is "Hospital Almendral". Although the hospital logo and name must be included in the business card, please make me a personal logo for myself. The logo might be maybe my name in a stylish font, or my initials (MAQB) or something like that. Im more inclined to a font logo, rather than a image logo, but a good one might change my mind. The info on my business card is going to be in spanish. The following info must be included please (the info within parenthesis is not to be included, it is provided for you to understand it since it's in spanish, so you can properly place it on the card):
-Dr. Mateo Anselmo Quiroga Benítez (my name)
-Medicina general (My specialty)
-Hospital Almendral (The name of the hospital where my office is)
-Calle Tomás Ibarrola #527 Col. Peñascal (address)
-Tel 471-5836 (Office phone)
-Sábado y domingo 10:00 am a 10:00pm (Office hours)
-Emergencias: 613-907-5148 (Emergency phone)
-mateoqb@correoandino.net (email)
-English Spoken
So, that's all the info i need to be on the business card. Although it's a business card for a doctor's office, i dont want it to be a boring, plain business card. Make it eye-catchy and stylish please. As i said, the hospital logo must be included. You'll find it on the heading of the PDF file i attached, but dont make it the center of attention.
Physician
Hello:My name is Dr. Mateo Anselmo Quiroga Benítez. I need a business card for my new office located within a hospital. The name of the hospital is "Hospital Almendral". Although the hospital logo and name must be included in the business card, please make me a personal logo for myself. The logo might be maybe my name in a stylish font, or my initials (MAQB) or something like that. Im more inclined to a font logo, rather than a image logo, but a good one might change my mind. The info on my business card is going to be in spanish. The following info must be included please (the info within parenthesis is not to be included, it is provided for you to understand it since it's in spanish, so you can properly place it on the card):-Dr. Mateo Anselmo Quiroga Benítez (my name)-Medicina general (My specialty)-Hospital Almendral (The name of the hospital where my office is)-Calle Tomás Ibarrola #527 Col. Peñascal (address)-Tel 471-5836 (Office phone)-Sábado y domingo 10:00 am a 10:00pm (Office hours)-Emergencias: 613-907-5148 (Emergency phone)-mateoqb@correoandino.net (email)-English Spoken So, that's all the info i need to be on the business card. Although it's a business card for a doctor's office, i dont want it to be a boring, plain business card. Make it eye-catchy and stylish please. As i said, the hospital logo must be included. You'll find it on the heading of the PDF file i attached, but dont make it the center of attention.

```html
<!DOCTYPE html>
<html lang="es">
<head>
<meta charset="utf-8">
<title>Tarjeta de presentación — Dr. Mateo Anselmo Quiroga Benítez</title>
<link rel="stylesheet" href="https://fonts.googleapis.com/css2?family=Cinzel:wght@600;700&family=Lato:wght@400;700&display=swap">
<style>
  :root {
    --navy: #0b3589;
    --navy-text: #133f92;
    --ink: #333a44;
    --card: #ffffff;
    --backdrop: #e9e8e6;
  }
  * { box-sizing: border-box; margin: 0; padding: 0; }
  html, body {
    width: 1200px;
    height: 900px;
    overflow: hidden;
    background: var(--backdrop);
  }
  .canvas {
    position: relative;
    width: 1200px;
    height: 900px;
  }
  .business-card {
    position: absolute;
    left: 120px;
    top: 153px;
    width: 960px;
    height: 594px;
    background: var(--card);
    box-shadow: 0 10px 30px rgba(0, 0, 0, 0.12);
    overflow: hidden;
  }
  .card-header {
    position: absolute;
    left: 0; top: 0;
    width: 100%;
    height: 132px;
    background: var(--navy);
    color: #fff;
    text-align: center;
  }
  .personal-monogram {
    position: absolute;
    left: 40px;
    top: 46px;
    display: flex;
    align-items: center;
    gap: 10px;
    font-family: "Cinzel", serif;
    font-weight: 700;
    font-size: 30px;
    letter-spacing: 2px;
    color: #fff;
  }
  .personal-monogram-dot {
    width: 12px;
    height: 12px;
    border-radius: 50%;
    background: #fff;
  }
  .doctor-name {
    font-family: "Cinzel", serif;
    font-weight: 700;
    font-size: 28px;
    letter-spacing: 0.5px;
    margin-top: 34px;
    line-height: 1.2;
  }
  .specialty {
    font-family: "Lato", sans-serif;
    font-size: 25px;
    margin-top: 4px;
  }
  .hospital-info {
    position: absolute;
    left: 53px;
    top: 190px;
    font-family: "Lato", sans-serif;
    font-style: normal;
    font-size: 25px;
    color: var(--ink);
    line-height: 35px;
  }
  .hospital-label {
    color: var(--navy-text);
    text-transform: uppercase;
  }
  .contact-list {
    position: absolute;
    left: 53px;
    top: 340px;
    list-style: none;
    font-family: "Lato", sans-serif;
    font-size: 25px;
    color: var(--ink);
  }
  .contact-item {
    display: flex;
    align-items: center;
    gap: 8px;
    height: 37px;
  }
  .contact-item--language { color: var(--navy-text); }
  .contact-icon {
    width: 30px;
    height: 30px;
    background: var(--navy);
    border-radius: 3px;
    display: flex;
    align-items: center;
    justify-content: center;
  }
  .hospital-mark {
    position: absolute;
    left: 440px;
    top: 172px;
    width: 480px;
    text-align: center;
  }
  .hospital-mark-square {
    display: block;
    width: 170px;
    height: 170px;
    margin: 0 auto 28px;
    background: var(--navy);
  }
  .hospital-mark-name {
    font-family: "Cinzel", serif;
    font-weight: 700;
    font-size: 40px;
    color: var(--navy);
    white-space: nowrap;
  }
  .card-footer {
    position: absolute;
    left: 0; bottom: 0;
    width: 100%;
    height: 112px;
    background: var(--navy);
    color: #fff;
    font-family: "Lato", sans-serif;
    font-size: 26px;
    display: flex;
    align-items: center;
    justify-content: center;
  }
</style>
</head>
<body>
<main class="canvas">
  <article class="business-card">
    <header class="card-header">
      <div class="personal-monogram"><span class="personal-monogram-dot"></span>MAQB</div>
      <h1 class="doctor-name">DR. MATEO ANSELMO QUIROGA BENÍTEZ</h1>
      <p class="specialty">Medicina general</p>
    </header>

    <address class="hospital-info">
      <div class="hospital-label">Hospital Almendral</div>
      <div>Calle Tomás Ibarrola #527</div>
      <div>Col. Peñascal</div>
    </address>

    <ul class="contact-list">
      <li class="contact-item">
        <span class="contact-icon">
          <svg width="20" height="20" viewBox="0 0 24 24" aria-hidden="true">
            <path fill="#fff" d="M6.6 10.8a15.1 15.1 0 0 0 6.6 6.6l2.2-2.2a1 1 0 0 1 1-.25 11.4 11.4 0 0 0 3.6.57 1 1 0 0 1 1 1V20a1 1 0 0 1-1 1A17 17 0 0 1 3 4a1 1 0 0 1 1-1h3.5a1 1 0 0 1 1 1c0 1.25.2 2.45.57 3.57a1 1 0 0 1-.25 1z"/>
          </svg>
        </span>
        <span>Tel 471-5836</span>
      </li>
      <li class="contact-item">
        <span class="contact-icon">
          <svg width="20" height="20" viewBox="0 0 24 24" aria-hidden="true">
            <rect x="3" y="6" width="18" height="12" fill="none" stroke="#fff" stroke-width="2"/>
            <path d="M3 6l9 7 9-7" fill="none" stroke="#fff" stroke-width="2"/>
          </svg>
        </span>
        <span>mateoqb@correoandino.net</span>
      </li>
      <li class="contact-item contact-item--language">
        <span class="contact-icon">
          <svg width="20" height="20" viewBox="0 0 24 24" aria-hidden="true">
            <path d="M4 5h16v10H10l-5 4v-4H4z" fill="none" stroke="#fff" stroke-width="2" stroke-linejoin="round"/>
          </svg>
        </span>
        <span>English Spoken</span>
      </li>
    </ul>

    <div class="hospital-mark">
      <span class="hospital-mark-square"></span>
      <div class="hospital-mark-name">Hospital Almendral</div>
    </div>

    <footer class="card-footer">
      Sábado y domingo 10:00 am a 10:00pm | Emergencias: 613-907-5148
    </footer>
  </article>
</main>
</body>
</html>
```